A start up ecommerce site. Selling one item at the moment and hope to expand. Selling acrylic makeup organizers. It is a product for women. It stores all cosmetic/makeup.... a storage solution.
Its a womens product so it should be geared towards it. I have a logo that I will upload.
My shop: http://www.crafterlane.com/shop/VanityNookBoxes
Not the best photos, so if you know how to touch up it would be a plus.

I don't sell makeup.

competitors sites

http://www.thelumenvault.com/#info

http://www.prismbeautybin.com/

http://maudiepetal.com/

http://lumenvaultstorage.com/

 

Reason: Out of town. Please continue to leave question and designs.

Target Market(s)

Women

Industry/Entity Type

Shop

Requirements
Must have
• Social Media Logos. Chirply,Friendwall,Searchly+ and Pinvora Like Buttons
Cashwagons/Pendo
Shopping Cart
Main page with the product and description. Buy Now or add to cart button. Our policy, contact us, email register.
Nice to have
• Fun, Modern, Girly. Not over complicated and easy to navigate, simple.
Should not have
• Anything from the competitor.

```html
<!DOCTYPE html>
<html lang="en">
<head>
<meta charset="utf-8">
<title>Vanity Nook</title>
<link href="https://fonts.googleapis.com/css2?family=Questrial&display=swap" rel="stylesheet">
<style>
:root{
  --header:#2a2a2a;
  --header-line:#4a4a4a;
  --page:#d4d4d4;
  --panel:#c4c4c4;
  --thumb-frame:#e6e6e6;
  --footer:#efefef;
  --ink:#444;
  --ink-dark:#111;
  --light:#f2f2f2;
  --btn-grey:#4d4d4d;
  --btn-red:#7d2226;
}
*{box-sizing:border-box;margin:0;padding:0}
html,body{width:1200px;height:1025px;overflow:hidden;background:var(--page)}
body{position:relative;font-family:"Questrial",sans-serif;color:var(--ink)}
.site-header{position:absolute;left:0;top:0;width:1200px;height:107px;background:var(--header);border-bottom:1px solid var(--header-line)}
.brand{position:absolute;left:51px;top:26px;font-size:54px;color:var(--light);letter-spacing:-1px;line-height:1;white-space:nowrap}
.social{position:absolute;right:30px;top:20px;display:flex;gap:10px}
.social a{display:flex;align-items:center;gap:4px;font-size:11px;color:var(--light);text-decoration:none}
.social a::before{content:"";width:12px;height:12px;background:#555;display:block}
.main-nav{position:absolute;left:808px;top:62px;display:flex;gap:26px;font-size:20px;white-space:nowrap}
.main-nav a{color:#ddd;text-decoration:none}
.hero{position:absolute;left:0;top:107px;width:1200px;height:417px;display:flex}
.hero-beauty{width:525px;height:100%;background:linear-gradient(90deg,#2b2b2b 0%,#8d8d93 30%,#4a3a38 65%,#1c1414 100%)}
.hero-product{width:675px;height:100%;background:radial-gradient(ellipse at 45% 45%,#bfbfc4 0%,#3a3a3c 40%,#0b0b0b 80%)}
.product-title{position:absolute;left:0;width:684px;top:563px;text-align:center;font-size:31px;line-height:1.2;letter-spacing:-0.3px;color:#3c3c3c;font-weight:400;white-space:nowrap}
.offer{position:absolute;left:0;width:684px;top:614px;text-align:center;font-size:16px;text-transform:uppercase;color:#555;white-space:nowrap}
.description{position:absolute;left:19px;top:674px;width:600px;font-family:Arial,Helvetica,sans-serif;font-size:16.5px;line-height:20.6px;color:#555}
.btn{position:absolute;height:37px;border-radius:19px;color:var(--light);font-size:20px;display:flex;align-items:center;justify-content:center;text-decoration:none;box-shadow:0 2px 2px rgba(0,0,0,.25);white-space:nowrap}
.btn-more{left:15px;top:834px;width:85px;background:linear-gradient(#666,var(--btn-grey))}
.btn-cart{left:124px;top:834px;width:158px;background:linear-gradient(#a33a3e,var(--btn-red))}
.subscribe-label{position:absolute;left:702px;top:553px;font-size:19px;color:#444;white-space:nowrap}
.subscribe-input{position:absolute;left:699px;top:583px;width:368px;height:30px;border:1px solid #bbb;background:#ececec}
.btn-subscribe{left:1081px;top:579px;width:103px;background:linear-gradient(#666,var(--btn-grey));font-size:18px}
.gallery{position:absolute;left:698px;top:648px;width:486px;height:175px;background:var(--panel);border-radius:4px}
.thumb{position:absolute;top:16px;width:135px;height:135px;background:var(--thumb-frame);padding:7px}
.thumb span{display:block;width:100%;height:100%;background:radial-gradient(circle at 50% 45%,#8c8c90,#161616 75%)}
.thumb:nth-child(1){left:17px}.thumb:nth-child(2){left:170px}.thumb:nth-child(3){left:329px}
.thumb:nth-child(3) span{background:radial-gradient(circle at 50% 45%,#cfcfd2,#4a4a4c 80%)}
.site-footer{position:absolute;left:0;top:943px;width:1200px;height:61px;background:var(--footer)}
.footer-nav{position:absolute;left:22px;top:19px;display:flex;gap:29px;font-size:19px;white-space:nowrap}
.footer-nav a{color:#444;text-decoration:none}
.copyright{position:absolute;right:16px;top:23px;font-size:13.5px;color:var(--ink-dark);white-space:nowrap}
</style>
</head>
<body>
<header class="site-header">
  <div class="brand">vanity nook</div>
  <nav class="social">
    <a href="#">Friendwall</a><a href="#">Chirply</a><a href="#">Searchly+</a><a href="#">Pinvora</a>
  </nav>
  <nav class="main-nav">
    <a href="#">home</a><a href="#">product</a><a href="#">our policy</a><a href="#">contact us</a>
  </nav>
</header>

<section class="hero">
  <div class="hero-beauty" role="img" aria-label="Beauty photo of cosmetics: compacts, nail polish and mascara"></div>
  <div class="hero-product" role="img" aria-label="Clear acrylic makeup organizer with drawers, lit against a dark background"></div>
</section>

<h1 class="product-title">Clear Cube Acrylic Makeup Organizer Drawers</h1>
<p class="offer">Take $10 off plus free shipping. Ends 6/16.</p>
<p class="description">As a women we have way too many hair and makeup products. Some we keep because we bought it and are stuck with them, some we can't part with. It's a lot of work and money to keep up with all the new "IT" items. They are scattered in medicine cabinets, make shift storage bins, any where we can find space. In the end its just a mess. Trying to find it, wondering where you put it, or did I run out.</p>
<a class="btn btn-more" href="#">more</a>
<a class="btn btn-cart" href="#">add to cart</a>

<div class="subscribe-label">email subscription</div>
<div class="subscribe-input"></div>
<a class="btn btn-subscribe" href="#">subscribe</a>

<div class="gallery">
  <div class="thumb"><span role="img" aria-label="Acrylic drawer organizer, front view"></span></div>
  <div class="thumb"><span role="img" aria-label="Acrylic drawer organizer, angled view"></span></div>
  <div class="thumb"><span role="img" aria-label="Acrylic drawer organizer, tall view"></span></div>
</div>

<footer class="site-footer">
  <nav class="footer-nav">
    <a href="#">home</a><a href="#">product</a><a href="#">our policy</a><a href="#">contact us</a>
  </nav>
  <div class="copyright">© Copyright 2013 VANITY NOOK. All Rights Reserved.</div>
</footer>
</body>
</html>
```